Hal's Remedies Business Card Design Project

I need a business card designed for my pharmacy Hal's Remedies. I would like just the logo on one side, maybe with black background and white lettering. The other side I would also like to include my logo which is attached. Also, please include my name and the following information:
Hal Norwick Owner/Pharm D.
Business address is 7163 N Birch Rd Sioux Falls, SD 57291.
Phone number is 605-318-6027 and fax # is 605-318-6031.
my email address is hal@halsremedies.example.
My website is www.halsremedies.example.
My business hours are Monday-Friday 8am-7 pm. Saturday 8am-12 pm. Sunday Closed.
I would like the design to include my logo colors, black, white, and neon green. Silver may be added as a highlight. Thanks.
Pharmacy
See above in product description

```html
<!DOCTYPE html>
<html lang="en">
<head>
<meta charset="utf-8">
<title>Hal's Remedies – Business Card</title>
<link rel="stylesheet" href="https://fonts.googleapis.com/css2?family=Open+Sans:wght@400;600;700&display=swap">
<style>
  :root {
    --ink: #000000;
    --paper: #ffffff;
    --neon: #8fd11a;
    --stage-light: #6a6a6a;
    --stage-dark: #1e1e1e;
    --card-radius: 22px;
  }
  html, body {
    margin: 0;
    padding: 0;
    width: 1200px;
    height: 820px;
    overflow: hidden;
  }
  body {
    position: relative;
    font-family: "Open Sans", Arial, sans-serif;
    background: radial-gradient(ellipse 70% 80% at 50% 40%, var(--stage-light) 0%, #3e3e3e 55%, var(--stage-dark) 100%);
  }
  .card {
    position: absolute;
    top: 258px;
    width: 471px;
    height: 270px;
    border-radius: var(--card-radius);
    overflow: hidden;
    box-shadow: 0 4px 10px rgba(0,0,0,0.55);
  }
  .card--front { left: 117px; background: var(--ink); }
  .card--back  { left: 629px; background: var(--ink); }

  .front-panels { position: absolute; inset: 0; }

  .brand-block {
    position: absolute;
    left: 20px;
    top: 92px;
    width: 200px;
    text-align: center;
  }
  .brand-dot {
    display: block;
    width: 16px;
    height: 16px;
    margin: 0 auto 10px;
    border-radius: 50%;
    background: var(--neon);
  }
  .brand-name {
    font-size: 26px;
    font-weight: 600;
    letter-spacing: -0.5px;
    color: var(--ink);
    white-space: nowrap;
  }

  .contact {
    position: absolute;
    right: 18px;
    top: 48px;
    text-align: right;
    color: var(--paper);
  }
  .contact__name {
    font-size: 18px;
    font-weight: 400;
    line-height: 24px;
  }
  .contact__title {
    font-size: 12.5px;
    color: var(--neon);
    line-height: 18px;
    padding-right: 1px;
  }
  .contact__address {
    margin-top: 21px;
    font-size: 11px;
    line-height: 18px;
    padding-right: 1px;
  }
  .contact__list {
    list-style: none;
    margin: 17px 0 0;
    padding: 0;
    font-size: 11px;
    line-height: 18.7px;
  }
  .contact__list li {
    display: flex;
    justify-content: flex-end;
    align-items: center;
    gap: 5px;
  }
  .contact__icon {
    width: 10px;
    height: 10px;
    flex: none;
  }

  .back-brand {
    position: absolute;
    left: 60px;
    top: 100px;
    display: flex;
    align-items: center;
    height: 66px;
  }
  .back-brand__dot {
    width: 22px;
    height: 22px;
    border-radius: 50%;
    background: var(--neon);
    margin: 0 36px 0 28px;
  }
  .back-brand__rule {
    width: 2px;
    height: 66px;
    background: var(--paper);
    margin-right: 16px;
  }
  .back-brand__name {
    font-size: 31px;
    font-weight: 600;
    letter-spacing: -0.6px;
    color: var(--paper);
    white-space: nowrap;
  }
  .hours {
    position: absolute;
    left: 0;
    right: 0;
    top: 215px;
    text-align: center;
    color: var(--paper);
    font-size: 11px;
    font-weight: 600;
    line-height: 15.5px;
    margin: 0;
  }
</style>
</head>
<body>

  <section class="card card--front" aria-label="Business card front">
    <svg class="front-panels" width="471" height="270" viewBox="0 0 471 270" aria-hidden="true">
      <polygon points="0,0 320,0 188,270 0,270" fill="#ffffff"/>
      <polygon points="319,0 323,0 213,270 188,270" fill="#8fd11a"/>
    </svg>

    <div class="brand-block">
      <span class="brand-dot"></span>
      <div class="brand-name">Hal's Remedies</div>
    </div>

    <div class="contact">
      <div class="contact__name">Hal Norwick</div>
      <div class="contact__title">Owner/Pharm D</div>
      <div class="contact__address">7163 N Birch Rd Sioux Falls,<br>SD 57291.</div>
      <ul class="contact__list">
        <li>605-318-6027
          <svg class="contact__icon" viewBox="0 0 10 10" aria-label="phone"><path d="M2 1 L4 1 L4.5 3 L3.3 4 Q4.5 6 6 6.7 L7 5.5 L9 6 L9 8 Q5 9 1 3 Z" fill="#8fd11a" transform="scale(-1,1) translate(-10,0)"/></svg>
        </li>
        <li>605-318-6031
          <svg class="contact__icon" viewBox="0 0 10 10" aria-label="fax"><rect x="1" y="4" width="8" height="5" fill="#8fd11a"/><rect x="3" y="1" width="4" height="3" fill="#8fd11a"/></svg>
        </li>
        <li>hal@halsremedies.example
          <svg class="contact__icon" viewBox="0 0 10 10" aria-label="email"><rect x="0.5" y="2" width="9" height="6.5" fill="#8fd11a"/><path d="M0.5 2 L5 5.8 L9.5 2" stroke="#000" stroke-width="0.9" fill="none"/></svg>
        </li>
        <li>www.halsremedies.example
          <svg class="contact__icon" viewBox="0 0 10 10" aria-label="website"><circle cx="5" cy="5" r="4.5" fill="#8fd11a"/><path d="M0.5 5 H9.5 M5 0.5 Q2.5 5 5 9.5 M5 0.5 Q7.5 5 5 9.5" stroke="#000" stroke-width="0.7" fill="none"/></svg>
        </li>
      </ul>
    </div>
  </section>

  <section class="card card--back" aria-label="Business card back">
    <div class="back-brand">
      <span class="back-brand__dot"></span>
      <span class="back-brand__rule"></span>
      <span class="back-brand__name">Hal's Remedies</span>
    </div>
    <p class="hours">business hours are: Monday-Friday 8am-7 pm.<br>Saturday 8am-12 pm. Sunday Closed.</p>
  </section>

</body>
</html>
```